VORELT B2B portal design
Fantastic design work, top communication and fast design changes! Many thanks,Jens & Uwe from VORELT
Zielgruppe
We are a B2B Cloud Services StartUp that creates B2B logistics & supply chain processes between customer and its suppliers.
Aufgabenstellung
We need a modern responsive able design, that should consider that we are NOT presenting goods or clothes or similar on the portal pages but we show mainly data grids, kpi dashboards, forms, and setting panels to our customer and their suppliers.
The design must be clean and straight not to distract people from the important information in these data grids, kpi dashboards, forms, and settings panels.
We need our logo perfectly embedded and the pages coloured around from grey to blue.
The Designer must be able to deliver a design and transfer it to a highly responsive HTML (5) template (without technical content or further functionality). This our programmers will implement afterwards in .Net.
We need in total 3 page templates:
1. Login Page
2. Main Page with overview over the following services text (each one shown in one tile)
"ZMS (Time Frame Management)"
"DMS (Document Management)"
"REMS (Reporting Management)"
-> Note: At the end we will have up to 12 or more tiles (services) so the design should be additive
3. Data grid (e.g. list of customers)/form (e.g. customer registration form) page to show some data grid with database data
See samples for each page enclosed!!

```html
<!DOCTYPE html>
<html lang="en">
<head>
<meta charset="utf-8">
<title>VORELT – Services</title>
<link rel="stylesheet" href="https://fonts.googleapis.com/css2?family=Open+Sans:wght@400;600;700&display=swap">
<style>
:root{
  --header-bg:#e2e7ea;
  --sidebar-bg:#e2e7ea;
  --content-bg:#f7f9fb;
  --navy:#0d2d4a;
  --text:#1c2b38;
  --muted:#4a5560;
  --line:#c9d0d6;
  --green:#5cb85c;
  --green-text:#3f9b3f;
  --blue:#4bafd2;
  --blue-text:#2b8cb0;
  --orange:#f0ad4e;
  --orange-text:#d4861d;
  --white:#ffffff;
}
*{box-sizing:border-box;margin:0;padding:0}
html,body{width:1200px;height:948px;overflow:hidden}
body{font-family:"Open Sans",Arial,sans-serif;background:var(--content-bg);color:var(--text);position:relative}
.topbar{position:absolute;left:0;top:0;width:1200px;height:138px;background:var(--header-bg);border-bottom:1px solid #9aa6b0}
.brand{position:absolute;left:20px;top:44px;display:flex;align-items:center;gap:12px;font-weight:700;font-size:40px;color:var(--navy);letter-spacing:1px}
.brand-dot{width:18px;height:18px;border-radius:50%;background:var(--navy)}
.user{position:absolute;right:24px;top:34px;display:flex;align-items:center}
.user-text{text-align:right;margin-right:10px}
.user-name{font-size:20px;font-weight:600;color:var(--text);line-height:24px}
.user-role{font-size:14px;color:var(--muted);line-height:18px}
.avatar{width:68px;height:68px;border-radius:50%;background:radial-gradient(circle at 50% 40%,#b89a86,#5c4a40 70%,#3a302a);border:2px solid #c3ccd3}
.caret{margin-left:10px;width:0;height:0;border-left:5px solid transparent;border-right:5px solid transparent;border-top:6px solid #6b7680}
.sidebar{position:absolute;left:0;top:138px;width:265px;height:708px;background:var(--sidebar-bg)}
.nav-item{height:61px;display:flex;align-items:center;padding-left:20px;border-bottom:1px solid var(--line);font-size:19px;color:var(--text)}
.nav-item svg{width:30px;height:24px;margin-right:6px;flex:none}
.nav-item.active{background:var(--navy);color:var(--white);border-bottom-color:var(--navy)}
.nav-item.active .chev{margin-left:auto;margin-right:28px;width:12px}
.tiles{position:absolute;left:304px;top:220px;display:flex;gap:36px}
.tile{width:264px;height:218px;background:var(--white);border:1px solid #d6dbe0;border-radius:3px;box-shadow:0 1px 2px rgba(0,0,0,.08);overflow:hidden;text-align:center}
.tile-visual{height:156px;display:flex;align-items:center;justify-content:center}
.tile-title{font-size:21px;font-weight:600;margin-top:7px;line-height:26px}
.tile-sub{font-size:15.5px;line-height:20px}
.tile.zms .tile-visual{background:var(--green)} .tile.zms{color:var(--green-text)}
.tile.dms .tile-visual{background:var(--blue)} .tile.dms{color:var(--blue-text)}
.tile.rems .tile-visual{background:var(--orange)} .tile.rems{color:var(--orange-text)}
.footer{position:absolute;left:0;top:888px;width:1200px;height:60px;background:var(--white);border-top:1px solid #e6e9ec;display:flex;align-items:center;justify-content:space-between;padding:0 22px 0 14px;font-size:17px;color:var(--muted)}
</style>
</head>
<body>
<header class="topbar">
  <div class="brand"><span class="brand-dot"></span>VORELT</div>
  <div class="user">
    <div class="user-text">
      <div class="user-name">Lena Marwick</div>
      <div class="user-role">Gest User</div>
    </div>
    <div class="avatar" role="img" aria-label="User profile photo"></div>
    <span class="caret"></span>
  </div>
</header>

<nav class="sidebar">
  <div class="nav-item"><svg viewBox="0 0 30 24"><circle cx="15" cy="12" r="9" fill="none" stroke="#0d2d4a" stroke-width="1.5"/><text x="15" y="15" font-size="8" font-weight="700" text-anchor="middle" fill="#0d2d4a" font-family="Open Sans,sans-serif">NEWS</text></svg>My News</div>
  <div class="nav-item"><svg viewBox="0 0 30 24"><circle cx="11" cy="7" r="5" fill="#0d2d4a"/><path d="M2 22c0-6 4-9 9-9s7 2 8 5v4z" fill="#0d2d4a"/><circle cx="22" cy="18" r="3.5" fill="none" stroke="#0d2d4a" stroke-width="2"/></svg>My User Settings</div>
  <div class="nav-item"><svg viewBox="0 0 30 24"><circle cx="10" cy="9" r="6" fill="none" stroke="#0d2d4a" stroke-width="4" stroke-dasharray="3 2"/><circle cx="21" cy="17" r="4" fill="none" stroke="#0d2d4a" stroke-width="3" stroke-dasharray="2 1.5"/></svg>Company Settings</div>
  <div class="nav-item"><svg viewBox="0 0 30 24"><path d="M5 21L18 8M14 3l7 7M18 21L6 6" stroke="#0d2d4a" stroke-width="3" stroke-linecap="round" fill="none"/></svg>Configuration</div>
  <div class="nav-item active"><svg viewBox="0 0 30 24"><g fill="#fff"><rect x="3" y="3" width="5" height="4"/><rect x="10" y="3" width="16" height="4"/><rect x="3" y="10" width="5" height="4"/><rect x="10" y="10" width="16" height="4"/><rect x="3" y="17" width="5" height="4"/><rect x="10" y="17" width="16" height="4"/></g></svg>Services<svg class="chev" viewBox="0 0 12 24"><path d="M3 7l5 5-5 5" stroke="#fff" stroke-width="2" fill="none"/></svg></div>
  <div class="nav-item"><svg viewBox="0 0 30 24"><path d="M4 11c0-5 5-8 10-8s10 3 10 8-5 8-10 8c-2 0-3 0-4-1l-6 3 2-5c-1-1-2-3-2-5z" fill="#0d2d4a"/></svg>Communication</div>
  <div class="nav-item"><svg viewBox="0 0 30 24"><path d="M15 4H6v16h16v-8" stroke="#0d2d4a" stroke-width="2.5" fill="none"/><path d="M12 14l11-11M16 3h7v7" stroke="#0d2d4a" stroke-width="2.5" fill="none"/></svg>Logout</div>
</nav>

<main class="tiles">
  <div class="tile zms">
    <div class="tile-visual">
      <svg width="110" height="110" viewBox="0 0 110 110" fill="none" stroke="#fff" stroke-width="6" stroke-linecap="round">
        <path d="M55 10a45 45 0 1 1-32 77"/>
        <path d="M23 87l2-14M23 87l14-1"/>
        <path d="M14 60a45 45 0 0 1 10-32" stroke-dasharray="4 8"/>
        <text x="55" y="68" font-size="30" fill="#fff" stroke="none" text-anchor="middle" font-family="Open Sans,sans-serif">24</text>
      </svg>
    </div>
    <div class="tile-title">ZMS</div>
    <div class="tile-sub">Time Frame Management System</div>
  </div>
  <div class="tile dms">
    <div class="tile-visual">
      <svg width="120" height="110" viewBox="0 0 120 110" fill="none" stroke="#fff" stroke-width="5" stroke-linejoin="round">
        <rect x="12" y="50" width="96" height="52"/>
        <path d="M12 50l14-24h68l14 24"/>
        <path d="M32 50V10h48v40M40 18h32"/>
        <circle cx="60" cy="76" r="7"/>
      </svg>
    </div>
    <div class="tile-title">DMS</div>
    <div class="tile-sub">Document Management System</div>
  </div>
  <div class="tile rems">
    <div class="tile-visual">
      <svg width="110" height="110" viewBox="0 0 110 110" fill="none" stroke="#fff" stroke-width="5" stroke-linejoin="round">
        <path d="M80 18h10v86H30V96"/>
        <rect x="18" y="6" width="62" height="90"/>
        <path d="M28 22h42M28 34h42"/>
        <path d="M32 72l12-12 12 14 16-20"/>
        <circle cx="32" cy="72" r="3" fill="#fff"/><circle cx="44" cy="60" r="3" fill="#fff"/><circle cx="56" cy="74" r="3" fill="#fff"/><circle cx="72" cy="54" r="3" fill="#fff"/>
      </svg>
    </div>
    <div class="tile-title">REMS</div>
    <div class="tile-sub">Reporting Management System</div>
  </div>
</main>

<footer class="footer">
  <span>© 2016 VORELT. All rights reserved.</span>
  <span>Help &nbsp;/&nbsp; Disclaimer &nbsp;/&nbsp; Contact</span>
</footer>
</body>
</html>
```